Copper Lantern Vapors - Premium labels

Copper Lantern Vapors is a business that has multiple retail locations where we sell e-cigs and liquid for e-cigs. We have our own house line of liquid but we're looking for expand our business with a premium brand of liquid. This label would be for our premium liquid bottles. We'd like to go with a Four Horseman of the Apocalypse theme. So I'm thinking we would have 4 flavors named White, Black, Red, and Pale.

Example label template attached.

Please let me know if you have any questions!

Thanks
(attaching our standard logo as reference)

Industry/Entity Type

Business

Requirements
Must have
• The branding should be for the Four Horseman theme. We want this to seem like it's own brand. Should have four different variations of labels - one each for White, Black, Red, and Pale. They can be very similar (or different), no preference at the moment.

```html
<!DOCTYPE html>
<html lang="en">
<head>
<meta charset="utf-8">
<title>Copper Lantern Vapors – Premium Labels</title>
<link href="https://fonts.googleapis.com/css2?family=Exo+2:wght@800&family=Montserrat:wght@600&family=Oswald:wght@400;600&family=Roboto+Condensed:wght@400;700&display=swap" rel="stylesheet">
<style>
  :root{
    --canvas:#d3d4d6;
    --black-head:#333232; --black-body:#4b4b4b; --black-art:#6a6a6a; --black-ink:#ffffff; --black-text:#e6e6e6; --black-small:#ffffff;
    --pale-head:#d97a62; --pale-body:#e48a72; --pale-art:#c9705c; --pale-ink:#7b2e28; --pale-text:#7b2e28; --pale-small:#ffffff;
    --white-head:#ffffff; --white-body:#e4e4e4; --white-art:#c9c9c9; --white-ink:#2d60ad; --white-text:#8a8a8a; --white-small:#333333;
    --red-head:#e93236; --red-body:#d63438; --red-art:#b8262b; --red-ink:#2c2a2a; --red-text:#2c2a2a; --red-small:#ffffff;
    --vapors-white:#9a9a9a;
  }
  *{margin:0;padding:0;box-sizing:border-box}
  html,body{width:1200px;height:1126px;overflow:hidden;background:var(--canvas)}
  .sheet{position:relative;width:1200px;height:1126px}
  .label{position:absolute;width:549px;height:509px;overflow:hidden;background:var(--body)}
  .label--black{left:28px;top:32px;--head:var(--black-head);--body:var(--black-body);--art:var(--black-art);--ink:var(--black-ink);--text:var(--black-text);--small:var(--black-small);--frame:#fff;--vapors:#d0d0d0}
  .label--pale{left:623px;top:32px;--head:var(--pale-head);--body:var(--pale-body);--art:var(--pale-art);--ink:var(--pale-ink);--text:var(--pale-text);--small:var(--pale-small);--frame:var(--pale-ink);--vapors:var(--pale-ink)}
  .label--white{left:28px;top:584px;--head:var(--white-head);--body:var(--white-body);--art:var(--white-art);--ink:var(--white-ink);--text:var(--white-text);--small:var(--white-small);--frame:#fff;--vapors:var(--vapors-white)}
  .label--red{left:623px;top:584px;--head:var(--red-head);--body:var(--red-body);--art:var(--red-art);--ink:var(--red-ink);--text:var(--red-text);--small:var(--red-small);--frame:#fff;--vapors:var(--red-ink)}

  .artwork{position:absolute;left:0;top:150px;width:549px;height:359px;
    background:radial-gradient(ellipse at 62% 45%, var(--art) 0%, transparent 70%), linear-gradient(180deg, var(--body), var(--art));
    opacity:.75}
  .header{position:absolute;left:0;top:0;width:549px;height:250px}
  .header path{fill:var(--head)}

  .mark{position:absolute;left:249px;top:72px;width:52px;height:52px;border-radius:50%;background:var(--ink)}
  .brand{position:absolute;left:0;width:549px;text-align:center}
  .brand__name{top:168px;font:800 24px/1 "Exo 2",sans-serif;color:var(--ink);letter-spacing:.5px}
  .brand__sub{top:200px;font:600 14px/1 "Montserrat",sans-serif;color:var(--vapors);letter-spacing:7px;padding-left:7px}

  .legal{position:absolute;left:12px;top:233px;height:262px;width:74px;writing-mode:vertical-rl;
    font:400 9.4px/12px "Roboto Condensed",sans-serif;color:var(--text);white-space:nowrap}
  .legal b{font-weight:700}

  .notice{position:absolute;left:487px;top:221px;width:45px;height:160px;border-left:1.5px solid var(--small);border-right:1.5px solid var(--small);
    writing-mode:vertical-rl;transform:rotate(180deg);display:flex;flex-direction:column;justify-content:center;gap:3px;
    font:400 9px/1.2 "Roboto Condensed",sans-serif;color:var(--small);text-align:left;padding:0 6px}
  .label--white .notice{border-color:#444;color:#333}

  .flag{position:absolute;left:489px;top:388px;width:42px;height:24px}
  .badges{position:absolute;left:485px;top:420px;width:52px;height:70px}

  .flavor{position:absolute;left:217px;top:371px;width:115px;height:64px;border:5px solid var(--frame);
    display:flex;align-items:center;justify-content:center;font:400 36px/1 "Oswald",sans-serif;color:var(--frame);letter-spacing:-1px}
  .label--white .flavor{border-color:#f4f4f4;color:#f4f4f4;outline:1px solid #cfcfcf}
  .volume{position:absolute;left:0;top:461px;width:549px;text-align:center;font:600 15px/1 "Oswald",sans-serif;color:#fff}
  .label--white .volume{color:#333}
</style>
</head>
<body>
<div class="sheet">

  <section class="label label--black">
    <div class="artwork" role="img" aria-label="Dark grey painted backdrop of mounted riders in a dramatic scene"></div>
    <svg class="header" viewBox="0 0 549 250" aria-hidden="true"><path d="M0 0H549V171Q274.5 317 0 171Z"/></svg>
    <div class="mark"></div>
    <div class="brand brand__name">COPPER LANTERN</div>
    <div class="brand brand__sub">VAPORS</div>
    <div class="legal"><b>Ingredients:</b> USP Grade Glycerin, USP Grade Propylene Glycol,<br>Natural &amp; Artificial Flavoring, USP Grade Nicotine <b>Prop 65</b><br><b>Warning:</b> This product may contain a chemical known to the<br>state of California to cause birth defects, or other reproductive harm.<br><b>NOT FOR UNDERAGE SALES</b><br><b>KEEP AWAY FROM CHILDREN AND PETS</b></div>
    <div class="notice"><span>WARNING: This product contains nicotine.</span><span>Nicotine is an addictive chemical.</span></div>
    <svg class="flag" viewBox="0 0 42 24" aria-hidden="true"><rect width="42" height="24" fill="#fff"/><g fill="#c8202f"><rect y="0" width="42" height="2.6"/><rect y="5.2" width="42" height="2.6"/><rect y="10.4" width="42" height="2.6"/><rect y="15.6" width="42" height="2.6"/><rect y="20.8" width="42" height="3.2"/></g><rect width="18" height="13" fill="#2b3a7a"/></svg>
    <svg class="badges" viewBox="0 0 52 70" aria-hidden="true"><g fill="none" stroke="#fff" stroke-width="1.5"><rect x="6" y="14" width="14" height="14" transform="rotate(45 13 21)"/><rect x="6" y="40" width="14" height="14" transform="rotate(45 13 47)"/><circle cx="38" cy="36" r="8"/><circle cx="38" cy="58" r="8"/></g><circle cx="38" cy="13" r="10" fill="#fff"/><text x="38" y="17" text-anchor="middle" font-family="Oswald,sans-serif" font-size="11" font-weight="600" fill="#333">21+</text><text x="13" y="25" text-anchor="middle" font-family="Oswald,sans-serif" font-size="10" fill="#fff">!</text></svg>
    <div class="flavor">Black</div>
    <div class="volume">2fl. oz. 60 ml</div>
  </section>

  <section class="label label--pale">
    <div class="artwork" role="img" aria-label="Salmon-tinted painted backdrop of mounted riders in a dramatic scene"></div>
    <svg class="header" viewBox="0 0 549 250" aria-hidden="true"><path d="M0 0H549V171Q274.5 317 0 171Z"/></svg>
    <div class="mark"></div>
    <div class="brand brand__name">COPPER LANTERN</div>
    <div class="brand brand__sub">VAPORS</div>
    <div class="legal"><b>Ingredients:</b> USP Grade Glycerin, USP Grade Propylene Glycol,<br>Natural &amp; Artificial Flavoring, USP Grade Nicotine <b>Prop 65</b><br><b>Warning:</b> This product may contain a chemical known to the<br>state of California to cause birth defects, or other reproductive harm.<br><b>NOT FOR UNDERAGE SALES</b><br><b>KEEP AWAY FROM CHILDREN AND PETS</b></div>
    <div class="notice"><span>WARNING: This product contains nicotine.</span><span>Nicotine is an addictive chemical.</span></div>
    <svg class="flag" viewBox="0 0 42 24" aria-hidden="true"><rect width="42" height="24" fill="#fff"/><g fill="#c8202f"><rect y="0" width="42" height="2.6"/><rect y="5.2" width="42" height="2.6"/><rect y="10.4" width="42" height="2.6"/><rect y="15.6" width="42" height="2.6"/><rect y="20.8" width="42" height="3.2"/></g><rect width="18" height="13" fill="#2b3a7a"/></svg>
    <svg class="badges" viewBox="0 0 52 70" aria-hidden="true"><g fill="none" stroke="#fff" stroke-width="1.5"><rect x="6" y="14" width="14" height="14" transform="rotate(45 13 21)"/><rect x="6" y="40" width="14" height="14" transform="rotate(45 13 47)"/><circle cx="38" cy="36" r="8"/><circle cx="38" cy="58" r="8"/></g><circle cx="38" cy="13" r="10" fill="#fff"/><text x="38" y="17" text-anchor="middle" font-family="Oswald,sans-serif" font-size="11" font-weight="600" fill="#7b2e28">21+</text><text x="13" y="25" text-anchor="middle" font-family="Oswald,sans-serif" font-size="10" fill="#fff">!</text></svg>
    <div class="flavor">Pale</div>
    <div class="volume">2fl. oz. 60 ml</div>
  </section>

  <section class="label label--white">
    <div class="artwork" role="img" aria-label="Faded light grey painted backdrop of mounted riders in a dramatic scene"></div>
    <svg class="header" viewBox="0 0 549 250" aria-hidden="true"><path d="M0 0H549V171Q274.5 317 0 171Z"/></svg>
    <div class="mark"></div>
    <div class="brand brand__name">COPPER LANTERN</div>
    <div class="brand brand__sub">VAPORS</div>
    <div class="legal"><b>Ingredients:</b> USP Grade Glycerin, USP Grade Propylene Glycol,<br>Natural &amp; Artificial Flavoring, USP Grade Nicotine <b>Prop 65</b><br><b>Warning:</b> This product may contain a chemical known to the<br>state of California to cause birth defects, or other reproductive harm.<br><b>NOT FOR UNDERAGE SALES</b><br><b>KEEP AWAY FROM CHILDREN AND PETS</b></div>
    <div class="notice"><span>WARNING: This product contains nicotine.</span><span>Nicotine is an addictive chemical.</span></div>
    <svg class="flag" viewBox="0 0 42 24" aria-hidden="true"><rect width="42" height="24" fill="#fff"/><g fill="#c8202f"><rect y="0" width="42" height="2.6"/><rect y="5.2" width="42" height="2.6"/><rect y="10.4" width="42" height="2.6"/><rect y="15.6" width="42" height="2.6"/><rect y="20.8" width="42" height="3.2"/></g><rect width="18" height="13" fill="#2b3a7a"/></svg>
    <svg class="badges" viewBox="0 0 52 70" aria-hidden="true"><g fill="none" stroke="#333" stroke-width="1.5"><rect x="6" y="14" width="14" height="14" transform="rotate(45 13 21)"/><rect x="6" y="40" width="14" height="14" transform="rotate(45 13 47)"/><circle cx="38" cy="36" r="8"/><circle cx="38" cy="58" r="8"/></g><circle cx="38" cy="13" r="10" fill="#333"/><text x="38" y="17" text-anchor="middle" font-family="Oswald,sans-serif" font-size="11" font-weight="600" fill="#fff">21+</text><text x="13" y="25" text-anchor="middle" font-family="Oswald,sans-serif" font-size="10" fill="#333">!</text></svg>
    <div class="flavor">White</div>
    <div class="volume">2fl. oz. 60 ml</div>
  </section>

  <section class="label label--red">
    <div class="artwork" role="img" aria-label="Red-tinted painted backdrop of mounted riders in a dramatic scene"></div>
    <svg class="header" viewBox="0 0 549 250" aria-hidden="true"><path d="M0 0H549V171Q274.5 317 0 171Z"/></svg>
    <div class="mark"></div>
    <div class="brand brand__name">COPPER LANTERN</div>
    <div class="brand brand__sub">VAPORS</div>
    <div class="legal"><b>Ingredients:</b> USP Grade Glycerin, USP Grade Propylene Glycol,<br>Natural &amp; Artificial Flavoring, USP Grade Nicotine <b>Prop 65</b><br><b>Warning:</b> This product may contain a chemical known to the<br>state of California to cause birth defects, or other reproductive harm.<br><b>NOT FOR UNDERAGE SALES</b><br><b>KEEP AWAY FROM CHILDREN AND PETS</b></div>
    <div class="notice"><span>WARNING: This product contains nicotine.</span><span>Nicotine is an addictive chemical.</span></div>
    <svg class="flag" viewBox="0 0 42 24" aria-hidden="true"><rect width="42" height="24" fill="#fff"/><g fill="#c8202f"><rect y="0" width="42" height="2.6"/><rect y="5.2" width="42" height="2.6"/><rect y="10.4" width="42" height="2.6"/><rect y="15.6" width="42" height="2.6"/><rect y="20.8" width="42" height="3.2"/></g><rect width="18" height="13" fill="#2b3a7a"/></svg>
    <svg class="badges" viewBox="0 0 52 70" aria-hidden="true"><g fill="none" stroke="#fff" stroke-width="1.5"><rect x="6" y="14" width="14" height="14" transform="rotate(45 13 21)"/><rect x="6" y="40" width="14" height="14" transform="rotate(45 13 47)"/><circle cx="38" cy="36" r="8"/><circle cx="38" cy="58" r="8"/></g><circle cx="38" cy="13" r="10" fill="#fff"/><text x="38" y="17" text-anchor="middle" font-family="Oswald,sans-serif" font-size="11" font-weight="600" fill="#d63438">21+</text><text x="13" y="25" text-anchor="middle" font-family="Oswald,sans-serif" font-size="10" fill="#fff">!</text></svg>
    <div class="flavor">Red</div>
    <div class="volume">2fl. oz. 60 ml</div>
  </section>

</div>
</body>
</html>
```